Building company buisness cards

We are looking for a sharp modern new look for our business cards.We are a New Zealand based company that specialises in house and land packages.We have attached a photo of the current logo and would like to see if it can be improved somehow if needed.We are open to any colours but we have chosen Black and White at this stage. Feel free to change the font and make the logo smarter looking.Play with the colours and see what looks best.We want a card that looks so good know one will want to throw it away!

Target Market(s)

Building profesonals, home buyers

Industry/Entity Type

Building

Contact Information for Business Card

Garrick Thorne
0274392068
garrickt@homevista.co.nz

Font styles to use
Serif
Sans Serif

Colors

Designer to choose colors to be used in the design.

Requirements
Must have
• Just the logo on one side and details on the other
• Clean simple looking card
Nice to have
• Round corners and detail like raised or spot UV
• Something that stands out
Should not have
• To title needed, Director etc

```html
<!DOCTYPE html>
<html lang="en">
<head>
<meta charset="utf-8">
<title>HomeVista Business Cards</title>
<link href="https://fonts.googleapis.com/css2?family=Playfair+Display:wght@900&family=Open+Sans:wght@400;700&display=swap" rel="stylesheet">
<style>
  :root {
    --backdrop: #2a2a2b;
    --card: #1b1b1c;
    --card-edge: #262627;
    --ink: #f2f2f2;
    --ink-soft: #c9c9c9;
    --silver: #d8d8d8;
    --divider: #5a5a5a;
  }
  * { margin: 0; padding: 0; box-sizing: border-box; }
  html, body { width: 1200px; height: 885px; overflow: hidden; }
  body {
    background: var(--backdrop);
    position: relative;
    font-family: "Open Sans", Arial, sans-serif;
  }
  .card {
    position: absolute;
    width: 540px;
    height: 310px;
    background: var(--card);
    border: 1px solid var(--card-edge);
    border-radius: 22px;
    box-shadow: 0 18px 40px rgba(0,0,0,0.45);
  }
  .card--front { left: 70px; top: 110px; }
  .card--back { left: 590px; top: 465px; }

  .front-mark {
    position: absolute;
    left: 0; right: 0; top: 92px;
    display: flex;
    justify-content: center;
    align-items: center;
    gap: 14px;
  }
  .front-mark__name {
    font-family: "Playfair Display", Georgia, serif;
    font-weight: 900;
    font-size: 70px;
    line-height: 1;
    color: var(--silver);
    letter-spacing: -1px;
  }
  .front-url {
    position: absolute;
    left: 0; right: 0; top: 222px;
    text-align: center;
    font-size: 12px;
    letter-spacing: 5px;
    color: var(--ink-soft);
  }

  .back-mark {
    position: absolute;
    left: 38px; top: 0; bottom: 0;
    width: 250px;
    display: flex;
    align-items: center;
    justify-content: center;
    gap: 10px;
  }
  .back-mark__circle {
    width: 26px; height: 26px;
    border: 3px solid var(--ink);
    border-radius: 50%;
    flex: none;
  }
  .back-mark__name {
    font-size: 34px;
    font-weight: 400;
    color: var(--ink);
    letter-spacing: 0.5px;
  }
  .divider {
    position: absolute;
    left: 300px; top: 62px;
    width: 1px; height: 186px;
    background: var(--divider);
  }
  .contact {
    position: absolute;
    left: 322px; top: 78px;
    color: var(--ink);
  }
  .contact__name {
    font-size: 19px;
    font-weight: 700;
    margin-bottom: 8px;
  }
  .contact__row {
    display: flex;
    align-items: center;
    gap: 8px;
    font-size: 14.5px;
    line-height: 22px;
    color: var(--ink);
  }
  .contact__row svg { width: 13px; height: 13px; flex: none; }
</style>
</head>
<body>
  <section class="card card--front" aria-label="Card front">
    <div class="front-mark">
      <span class="front-mark__name">HomeVista</span>
    </div>
    <p class="front-url">www.homevista.co.nz</p>
  </section>

  <section class="card card--back" aria-label="Card back">
    <div class="back-mark">
      <span class="back-mark__circle"></span>
      <span class="back-mark__name">HomeVista</span>
    </div>
    <div class="divider"></div>
    <div class="contact">
      <p class="contact__name">Garrick Thorne</p>
      <p class="contact__row">
        <svg viewBox="0 0 16 16" aria-hidden="true"><path fill="#f2f2f2" d="M3 2h3l1 3-2 1.5c.8 1.8 2.3 3.3 4 4L10.5 9l3 1v3c0 .6-.4 1-1 1C7 14 2 9 2 3c0-.6.4-1 1-1z"/></svg>
        0274392068
      </p>
      <p class="contact__row">
        <svg viewBox="0 0 16 16" aria-hidden="true"><rect x="1" y="3" width="14" height="10" fill="#f2f2f2"/><path d="M1 3l7 6 7-6" fill="none" stroke="#1b1b1c" stroke-width="1.4"/></svg>
        garrickt@homevista.co.nz
      </p>
      <p class="contact__row">
        <svg viewBox="0 0 16 16" aria-hidden="true"><circle cx="8" cy="8" r="7" fill="#f2f2f2"/><path d="M1 8h14M8 1c-3 3.5-3 10.5 0 14M8 1c3 3.5 3 10.5 0 14" fill="none" stroke="#1b1b1c" stroke-width="1.2"/></svg>
        www.homevista.co.nz
      </p>
    </div>
  </section>
</body>
</html>
```